Lark Ridge Property Biz Card
Business card and stationary
Project: Lark Ridge Property Biz Card
Lark Ridge Property Biz Card - Real Estate
Creative Brief
Professional
Dwight Fenmore
DO NOT ADD AN ADDRESS
dfenmore@larkridgeproperty.com
On the front I would like the logo, my name, phone number and email address. Also please have the catch phrase: "We buy houses, any condition! Get Cash Fast! Quick Closing!" The colour scheme of my logo is not set in stone, so please feel free to experiment with the colours.
On the back of the card please have the company logo

```html
<!DOCTYPE html>
<html lang="en">
<head>
<meta charset="utf-8">
<title>Lark Ridge Property – Business Card</title>
<link rel="stylesheet" href="https://fonts.googleapis.com/css2?family=Open+Sans:ital,wght@0,400;0,700;1,700&display=swap">
<style>
  :root {
    --brand-blue: #1f4f8f;
    --ink: #1d1d1f;
    --muted: #6b6b6b;
    --divider: #c9c9c9;
    --swoosh-grey: #b9b9bb;
    --card: #ffffff;
    --backdrop: #e6e6e8;
  }
  * { margin: 0; padding: 0; box-sizing: border-box; }
  html, body {
    width: 1200px;
    height: 780px;
    overflow: hidden;
    background: var(--backdrop);
    font-family: "Open Sans", Arial, sans-serif;
  }
  .canvas {
    position: relative;
    width: 1200px;
    height: 780px;
  }
  .business-card {
    position: absolute;
    left: 100px;
    top: 104px;
    width: 1000px;
    height: 572px;
    background: var(--card);
    border-radius: 28px 56px 28px 56px;
    overflow: hidden;
    box-shadow: 0 10px 30px rgba(0,0,0,0.18);
  }
  .brand-mark {
    position: absolute;
    left: 40px;
    top: 150px;
    width: 290px;
    display: flex;
    align-items: center;
    gap: 14px;
  }
  .brand-mark__square {
    flex: none;
    width: 26px;
    height: 26px;
    background: var(--brand-blue);
  }
  .brand-mark__name {
    color: var(--brand-blue);
    font-weight: 700;
    font-size: 34px;
    line-height: 1.1;
  }
  .divider {
    position: absolute;
    left: 362px;
    top: 80px;
    width: 1px;
    height: 260px;
    background: var(--divider);
  }
  .contact {
    position: absolute;
    left: 398px;
    top: 104px;
  }
  .contact__name {
    color: var(--brand-blue);
    font-weight: 700;
    font-size: 34px;
    line-height: 1.15;
  }
  .contact__title {
    color: var(--muted);
    font-size: 21px;
    margin-top: 2px;
  }
  .contact__lines {
    list-style: none;
    margin-top: 56px;
  }
  .contact__line {
    display: flex;
    align-items: center;
    gap: 14px;
    color: var(--ink);
    font-size: 21px;
    margin-bottom: 16px;
  }
  .contact__icon {
    width: 22px;
    height: 22px;
    flex: none;
    color: var(--ink);
  }
  .slogan {
    position: absolute;
    left: 0;
    right: 0;
    top: 384px;
    text-align: center;
    color: var(--ink);
    font-weight: 700;
    font-style: italic;
    font-size: 23px;
    line-height: 1.35;
    padding-left: 60px;
  }
  .swoosh {
    position: absolute;
    left: 0;
    bottom: 0;
    width: 1000px;
    height: 572px;
  }
</style>
</head>
<body>
<main class="canvas">
  <section class="business-card" aria-label="Lark Ridge Property business card">
    <svg class="swoosh" viewBox="0 0 1000 572" preserveAspectRatio="none" aria-hidden="true">
      <path d="M0,470 C280,555 640,525 1000,420 L1000,572 L0,572 Z" fill="var(--swoosh-grey)"/>
      <path d="M0,535 C330,585 700,540 1000,448 L1000,572 L0,572 Z" fill="var(--brand-blue)"/>
    </svg>

    <div class="brand-mark">
      <span class="brand-mark__square" aria-hidden="true"></span>
      <span class="brand-mark__name">Lark Ridge Property</span>
    </div>

    <div class="divider" aria-hidden="true"></div>

    <div class="contact">
      <h1 class="contact__name">Dwight Fenmore</h1>
      <p class="contact__title">your title</p>
      <ul class="contact__lines">
        <li class="contact__line">
          <svg class="contact__icon" viewBox="0 0 24 24" aria-hidden="true">
            <path fill="currentColor" d="M6.6 10.8a15.1 15.1 0 0 0 6.6 6.6l2.2-2.2c.3-.3.7-.4 1-.2 1.1.4 2.3.6 3.6.6.6 0 1 .4 1 1V20c0 .6-.4 1-1 1C10.6 21 3 13.4 3 4c0-.6.4-1 1-1h3.5c.6 0 1 .4 1 1 0 1.3.2 2.5.6 3.6.1.3 0 .7-.2 1z"/>
          </svg>
          <span>204-555-0187</span>
        </li>
        <li class="contact__line">
          <svg class="contact__icon" viewBox="0 0 24 24" aria-hidden="true">
            <circle cx="12" cy="12" r="4" fill="none" stroke="currentColor" stroke-width="2.4"/>
            <path d="M16 8v5.5a2.5 2.5 0 0 0 5 0V12a9 9 0 1 0-3.5 7.1" fill="none" stroke="currentColor" stroke-width="2.4" stroke-linecap="round"/>
          </svg>
          <span>dfenmore@larkridgeproperty.com</span>
        </li>
      </ul>
    </div>

    <p class="slogan">"We buy houses, any condition!<br>Get Cash Fast! Quick Closing!"</p>
  </section>
</main>
</body>
</html>
```